INFOGRAPHIC DESING GYM SCHEDULE . FULL SCHEDULE AND CLASSES ROON SCHEDULE

I NEED TO CREATED A DESIGN FOR COMPLETE SCHEDULE TAMPLE FOR OUR GYM
AND SMALL SCHEDULE FOR EACH ROON OF THE GYM AND THE CLASSES THTA HAPPEN IN THE ROON
THE SCHEDULE WILL HAVE
CLASSES SCHEDULE
CLASSE DESCRIPTION
AND GRAPHIC EXPLAN HOW EFFECTIVE THE CLASSES ARE IN SOME IMPORT FECTOR .
I MAKE MY SELF A SAMPLE AND WILL UP LOAD IT NO WEEL DONE, BUT YOU CAN HAVE AN IDEIA
II LIKE TO MAKE IT BETTER AND MORE PROFESSIONAL .
RIGHT NOW WE CAN HAVE ALL AS PLACE HOLDER
Updates

hello i never got any other file right now i am very frustrated with this servese i spend a lot of monet for a design this experience is far from been good

Target Market(s)

gym

Font styles to use
Sans Serif

Colors
ec1f27
000000
9d9d9d

Requirements
Must have
• MUST HAVE A UNIQUE DESIGN . WILL USE ALL OF OUR GYM AND WILL NEED TO HAVE A PERSOLIZED DESIGN .
• WE NEED TO HAVE A TAMPLE WHERE WE CAN CHAGE OUR SELF BECOUSE THE CLASSE SCHEDULE CHANGE OTHER TIME
Nice to have
• THE GRAFIC EXPLAN HOW EFECTIVE THE CLASSES ARE IN EXTREMILY IMPORTANT. WE WANT TO INOVAT AND CRETED SOMETIMNH UNIQUE
• I UP LOAD OUR LOGO, IS SHOULD TO FOLOW OUR COLORS
• ON THE SCHEDUDLE SHOULD HAVE A LOGO

```html
<!DOCTYPE html>
<html lang="en">
<head>
<meta charset="utf-8">
<title>Bike Room Schedule</title>
<link href="https://fonts.googleapis.com/css2?family=Russo+One&family=Montserrat:wght@400;500;600;700;800&family=Oswald:wght@500&family=Open+Sans:wght@400;600&display=swap" rel="stylesheet">
<style>
  :root{
    --red:#ec1f27;
    --black:#000000;
    --grey:#9d9d9d;
    --cell-light:#f6f6f6;
    --cell-dark:#ebebeb;
    --head-grey:#ececec;
    --white:#ffffff;
    --m1:#f8e04c; --m2:#f0bb3a; --m3:#f28b1f; --m4:#ef5b24; --m5:#e03425; --m6:#b71c1c;
  }
  *{margin:0;padding:0;box-sizing:border-box}
  html,body{width:848px;height:1200px;overflow:hidden;background:var(--white)}
  .sheet{position:relative;width:848px;height:1200px;overflow:hidden;font-family:'Montserrat',sans-serif;color:var(--black)}

  /* Header */
  .brand{position:absolute;left:20px;top:44px;display:flex;align-items:center;gap:7px}
  .brand-dot{width:40px;height:40px;border-radius:50%;background:var(--grey)}
  .brand-name{font-family:'Montserrat',sans-serif;font-weight:700;font-size:12px;line-height:1.15;color:var(--grey);width:100px}
  .title{position:absolute;left:176px;top:34px;font-family:'Russo One',sans-serif;font-size:66px;line-height:1;letter-spacing:1px;transform:skewX(-12deg);white-space:nowrap}
  .title .accent{color:var(--red)}
  .title-band{position:absolute;left:0;top:0}
  .subtitle{position:absolute;left:290px;top:116px;width:360px;text-align:center;font-family:'Russo One',sans-serif;font-size:30px;letter-spacing:16px;color:var(--white);transform:skewX(-12deg)}
  .rider-art{position:absolute;left:668px;top:20px;width:122px;height:156px;border-radius:40% 40% 30% 30%;background:radial-gradient(circle at 50% 55%,#3a3a3a,#000 70%,transparent 72%)}

  /* Schedule */
  .days,.row{position:absolute;left:160px;display:grid;grid-template-columns:repeat(6,108px);column-gap:2px}
  .days{top:166px;height:31px}
  .day{background:var(--red);color:var(--white);font-weight:600;font-size:14px;display:flex;align-items:center;justify-content:center}
  .row .cell{display:flex;align-items:center;justify-content:center;text-align:center;font-size:12.5px;line-height:1.2;font-weight:400;text-transform:uppercase}
  .row.light .cell{background:var(--cell-light)}
  .row.dark .cell{background:var(--cell-dark)}
  .r1{top:198px;height:44px}
  .r2{top:242px;height:43px}
  .r3{top:314px;height:46px}
  .r4{top:360px;height:44px}
  .afternoon{position:absolute;left:160px;top:286px;width:658px;height:26px;background:var(--black);color:var(--white);font-weight:700;font-size:13px;letter-spacing:9px;display:flex;align-items:center;justify-content:center}
  .time{position:absolute;left:32px;width:111px;height:35px;background:var(--black);color:var(--white);font-weight:600;font-size:24px;display:flex;align-items:center;padding-left:18px;clip-path:polygon(0 0,88% 0,100% 50%,88% 100%,0 100%)}

  /* Definitions */
  .definitions{position:absolute;left:0;top:446px;width:848px;height:251px;background:var(--black);color:var(--white)}
  .section-title{position:absolute;left:0;width:848px;text-align:center;font-family:'Russo One',sans-serif;font-size:32px;letter-spacing:3px}
  .section-title span{display:inline-block;transform:skewX(-12deg)}
  .dash{position:absolute;height:8px;width:80px;background:var(--red);transform:skewX(-20deg)}
  .definitions .section-title{top:19px}
  .def{position:absolute;top:82px;width:240px;text-align:center}
  .def h3{font-family:'Russo One',sans-serif;font-weight:400;font-size:17px;letter-spacing:2px;transform:skewX(-12deg);margin-bottom:10px}
  .def p{font-family:'Open Sans',sans-serif;font-size:12px;line-height:17px;text-transform:uppercase}
  .def-rule{position:absolute;top:92px;width:3px;height:130px;background:var(--red);transform:rotate(6deg)}

  /* Intensity */
  .intensity-title{top:718px}
  .intensity-title .accent{color:var(--red)}
  .metrics{position:absolute;left:28px;display:grid;grid-template-columns:94px repeat(4,165px);column-gap:11px}
  .metrics.top{top:786px}
  .metrics.bottom{top:984px}
  .metric-head{grid-row:1;height:22px;background:var(--head-grey);font-weight:500;font-size:15px;display:flex;align-items:center;justify-content:center;text-transform:uppercase}
  .corner{grid-row:1}
  .tag{align-self:start;width:94px;height:21px;margin-top:6px;background:var(--red);color:var(--white);font-family:'Oswald',sans-serif;font-weight:500;font-size:11.5px;line-height:1;white-space:nowrap;display:flex;align-items:center;justify-content:center;padding:0 10px 0 2px;clip-path:polygon(0 0,89% 0,100% 50%,89% 100%,0 100%);text-transform:uppercase}
  .meter{height:50px;position:relative;padding-top:10px}
  .bar{height:13px;background:linear-gradient(90deg,var(--m1) 0 16.66%,var(--m2) 16.66% 33.33%,var(--m3) 33.33% 50%,var(--m4) 50% 66.66%,var(--m5) 66.66% 83.33%,var(--m6) 83.33% 100%)}
  .marker{position:absolute;top:2px;width:0;height:0;border-left:5px solid transparent;border-right:5px solid transparent;border-top:6px solid var(--black);transform:translateX(-50%)}
  .low .marker{left:8.3%}
  .med .marker{left:50%}
  .high .marker{left:91.7%}
  .scale{display:flex;justify-content:space-between;font-size:8.5px;font-weight:700;margin-top:4px}
</style>
</head>
<body>
<div class="sheet">

  <svg class="title-band" width="848" height="200" aria-hidden="true">
    <polygon points="48,145 164,145 162,152 46,152" fill="var(--red)"/>
    <polygon points="172,114 655,114 640,152 158,152" fill="var(--red)"/>
  </svg>

  <div class="brand">
    <div class="brand-dot"></div>
    <div class="brand-name">SUMMIT TRAINING CENTER</div>
  </div>

  <div class="title">BIKE <span class="accent">ROOM</span></div>
  <div class="subtitle">SCHEDULE</div>
  <div class="rider-art" role="img" aria-label="Silhouette illustration of a cyclist riding a road bike"></div>

  <div class="days">
    <div class="day">MONDAY</div><div class="day">TUESDAY</div><div class="day">WEDNESDAY</div>
    <div class="day">THURSDAY</div><div class="day">FRIDAY</div><div class="day">SATURDAY</div>
  </div>

  <div class="time" style="top:200px">8:30</div>
  <div class="time" style="top:246px">9:30</div>
  <div class="time" style="top:320px">5:30</div>
  <div class="time" style="top:366px">6:30</div>

  <div class="row light r1">
    <div class="cell">Saw</div><div class="cell">Hiit Cycling</div><div class="cell">Saw</div>
    <div class="cell">Hiit Cycling</div><div class="cell">Saw</div><div class="cell"></div>
  </div>
  <div class="row dark r2">
    <div class="cell">Indoor<br>Cycling</div><div class="cell">Saw</div><div class="cell">Indoor<br>Cycling</div>
    <div class="cell">Saw</div><div class="cell">Indoor<br>Cycling</div><div class="cell">Saw</div>
  </div>
  <div class="afternoon">AFTERNOON SCHEDULE</div>
  <div class="row light r3">
    <div class="cell">Hiit Cycling</div><div class="cell">Saw</div><div class="cell">Hiit Cycling</div>
    <div class="cell">Saw</div><div class="cell">Hiit Cycling</div><div class="cell"></div>
  </div>
  <div class="row dark r4">
    <div class="cell">Saw</div><div class="cell">Indoor<br>Cycling</div><div class="cell">Saw</div>
    <div class="cell">Indoor<br>Cycling</div><div class="cell">Saw</div><div class="cell"></div>
  </div>

  <section class="definitions">
    <div class="dash" style="left:56px;top:36px"></div>
    <div class="dash" style="left:712px;top:36px"></div>
    <h2 class="section-title"><span>CLASSES DEFINITION</span></h2>

    <div class="def" style="left:27px">
      <h3>SAW</h3>
      <p>Kids boxing class teach basic boxing skills and techniques such as; stance, guard, movement, jab, cross, hook. It increases strength and improves indurance.</p>
    </div>
    <div class="def-rule" style="left:294px"></div>
    <div class="def" style="left:304px">
      <h3>HIIT CYCLING</h3>
      <p>Kids boxing class teach basic boxing skills and techniques such as; stance, guard, movement, jab, cross, hook. It increases strength and improves indurance.</p>
    </div>
    <div class="def-rule" style="left:572px"></div>
    <div class="def" style="left:583px">
      <h3>INDOOR CYCLING</h3>
      <p>Kids boxing class teach basic boxing skills and techniques such as; stance, guard, movement, jab, cross, hook. It increases strength and improves indurance.</p>
    </div>
  </section>

  <div class="dash" style="left:56px;top:736px"></div>
  <div class="dash" style="left:712px;top:736px"></div>
  <h2 class="section-title intensity-title"><span><span class="accent">CLASSES</span> FINTENSITY</span></h2>

  <div class="metrics top">
    <div class="corner"></div>
    <div class="metric-head">Fat Burn</div><div class="metric-head">Intersnity</div>
    <div class="metric-head">Cardio</div><div class="metric-head">Agility</div>

    <div class="tag">SAW</div>
    <div class="meter high"><span class="marker"></span><div class="bar"></div><div class="scale"><span>LOW</span><span>MEDIUM</span><span>HIGH</span></div></div>
    <div class="meter high"><span class="marker"></span><div class="bar"></div><div class="scale"><span>LOW</span><span>MEDIUM</span><span>HIGH</span></div></div>
    <div class="meter high"><span class="marker"></span><div class="bar"></div><div class="scale"><span>LOW</span><span>MEDIUM</span><span>HIGH</span></div></div>
    <div class="meter high"><span class="marker"></span><div class="bar"></div><div class="scale"><span>LOW</span><span>MEDIUM</span><span>HIGH</span></div></div>

    <div class="tag">HIT CYCLING</div>
    <div class="meter high"><span class="marker"></span><div class="bar"></div><div class="scale"><span>LOW</span><span>MEDIUM</span><span>HIGH</span></div></div>
    <div class="meter high"><span class="marker"></span><div class="bar"></div><div class="scale"><span>LOW</span><span>MEDIUM</span><span>HIGH</span></div></div>
    <div class="meter high"><span class="marker"></span><div class="bar"></div><div class="scale"><span>LOW</span><span>MEDIUM</span><span>HIGH</span></div></div>
    <div class="meter med"><span class="marker"></span><div class="bar"></div><div class="scale"><span>LOW</span><span>MEDIUM</span><span>HIGH</span></div></div>

    <div class="tag">INDOOR CYCLING</div>
    <div class="meter high"><span class="marker"></span><div class="bar"></div><div class="scale"><span>LOW</span><span>MEDIUM</span><span>HIGH</span></div></div>
    <div class="meter med"><span class="marker"></span><div class="bar"></div><div class="scale"><span>LOW</span><span>MEDIUM</span><span>HIGH</span></div></div>
    <div class="meter med"><span class="marker"></span><div class="bar"></div><div class="scale"><span>LOW</span><span>MEDIUM</span><span>HIGH</span></div></div>
    <div class="meter med"><span class="marker"></span><div class="bar"></div><div class="scale"><span>LOW</span><span>MEDIUM</span><span>HIGH</span></div></div>
  </div>

  <div class="metrics bottom">
    <div class="corner"></div>
    <div class="metric-head">Balance</div><div class="metric-head">Flexibility</div>
    <div class="metric-head">Power</div><div class="metric-head">Contact</div>

    <div class="tag">SAW</div>
    <div class="meter med"><span class="marker"></span><div class="bar"></div><div class="scale"><span>LOW</span><span>MEDIUM</span><span>HIGH</span></div></div>
    <div class="meter med"><span class="marker"></span><div class="bar"></div><div class="scale"><span>LOW</span><span>MEDIUM</span><span>HIGH</span></div></div>
    <div class="meter med"><span class="marker"></span><div class="bar"></div><div class="scale"><span>LOW</span><span>MEDIUM</span><span>HIGH</span></div></div>
    <div class="meter low"><span class="marker"></span><div class="bar"></div><div class="scale"><span>LOW</span><span>MEDIUM</span><span>HIGH</span></div></div>

    <div class="tag">HIT CYCLING</div>
    <div class="meter med"><span class="marker"></span><div class="bar"></div><div class="scale"><span>LOW</span><span>MEDIUM</span><span>HIGH</span></div></div>
    <div class="meter med"><span class="marker"></span><div class="bar"></div><div class="scale"><span>LOW</span><span>MEDIUM</span><span>HIGH</span></div></div>
    <div class="meter low"><span class="marker"></span><div class="bar"></div><div class="scale"><span>LOW</span><span>MEDIUM</span><span>HIGH</span></div></div>
    <div class="meter low"><span class="marker"></span><div class="bar"></div><div class="scale"><span>LOW</span><span>MEDIUM</span><span>HIGH</span></div></div>

    <div class="tag">INDOOR CYCLING</div>
    <div class="meter low"><span class="marker"></span><div class="bar"></div><div class="scale"><span>LOW</span><span>MEDIUM</span><span>HIGH</span></div></div>
    <div class="meter low"><span class="marker"></span><div class="bar"></div><div class="scale"><span>LOW</span><span>MEDIUM</span><span>HIGH</span></div></div>
    <div class="meter low"><span class="marker"></span><div class="bar"></div><div class="scale"><span>LOW</span><span>MEDIUM</span><span>HIGH</span></div></div>
    <div class="meter low"><span class="marker"></span><div class="bar"></div><div class="scale"><span>LOW</span><span>MEDIUM</span><span>HIGH</span></div></div>
  </div>

</div>
</body>
</html>
```